Solar energy proposal for homeowners

I am providing households with solar energy proposals, and I need a high-quality brochure that is packaged cleverly to attract the homeowner's attention. Take a look at the one page solar brochure that I have included to get an idea of text and content.

Target Market(s)

Residential Homeowners

Industry/Entity Type

Solar

Requirements
Must have
• High quality document

```html
<!DOCTYPE html>
<html lang="en">
<head>
<meta charset="utf-8">
<title>Brightvale Energy – Solar Flyer</title>
<link href="https://fonts.googleapis.com/css2?family=Red+Hat+Display:wght@400;700;900&family=Montserrat:wght@300;400;500;600&display=swap" rel="stylesheet">
<style>
  :root{
    --cyan:#079fd5;
    --cyan-light:#13b3d6;
    --navy:#26386d;
    --navy-text:#1f3468;
    --green:#8cc152;
    --teal:#2ab7b4;
    --ink:#2f3440;
    --paper:#ffffff;
    --backdrop:#ecebe7;
    --photo-roof:#4a4e60;
    --photo-garden:#6f9a4a;
  }
  *{margin:0;padding:0;box-sizing:border-box}
  html,body{width:1200px;height:1117px;overflow:hidden;background:var(--backdrop)}
  .stage{position:relative;width:1200px;height:1117px}
  .flyer{
    position:absolute;left:219px;top:20px;width:1058px;height:1495px;
    transform:scale(0.7204);transform-origin:0 0;
    background:var(--paper);overflow:hidden;
    font-family:"Montserrat",sans-serif;color:var(--ink);
  }
  .shapes,.photo{position:absolute;left:0;top:0}
  .brand{position:absolute;left:95px;top:62px;display:flex;align-items:center;gap:16px}
  .brand-mark{width:60px;height:60px;background:var(--teal)}
  .brand-name{font-family:"Montserrat",sans-serif;font-weight:400;font-size:58px;color:var(--teal);letter-spacing:-0.5px}
  .headline{position:absolute;left:95px;top:212px;font-family:"Red Hat Display",sans-serif;font-weight:900;
    font-size:52px;line-height:52px;color:#fff;letter-spacing:-0.5px}
  .tagline{position:absolute;left:95px;top:428px;font-family:"Montserrat",sans-serif;font-weight:400;
    font-size:38px;line-height:41px;color:#fff}
  .section-title{position:absolute;left:0;width:1058px;top:582px;text-align:center;
    font-family:"Red Hat Display",sans-serif;font-weight:900;font-size:30px;color:var(--navy-text)}
  .rule{position:absolute;top:598px;height:3px;background:linear-gradient(90deg,var(--cyan),var(--green))}
  .about-text{position:absolute;left:110px;width:838px;top:617px;text-align:center;font-size:19.5px;line-height:23.5px;color:#333}
  .tab{position:absolute;top:750px;height:46px;width:368px;display:flex;align-items:center;justify-content:center;
    background:linear-gradient(90deg,var(--cyan),var(--green));font-family:"Red Hat Display",sans-serif;font-weight:900;
    font-size:30px;color:#fff}
  .services{position:absolute;left:100px;top:828px;width:420px}
  .service{position:absolute;left:0;display:flex;gap:28px;width:420px}
  .service svg{flex:none}
  .service h3{font-family:"Montserrat",sans-serif;font-weight:600;font-size:22px;color:#fff;margin-top:-2px;margin-bottom:6px}
  .service p{font-size:19.5px;line-height:23.5px;color:#fff;font-weight:400}
  .benefits{position:absolute;left:585px;top:814px;list-style:none}
  .benefits li{display:flex;align-items:center;gap:18px;font-size:20.5px;height:34px;color:#333}
  .contact{position:absolute;left:0;top:1365px;width:1058px;height:78px;display:flex;align-items:center;justify-content:center;
    gap:16px;font-family:"Red Hat Display",sans-serif;font-weight:700;font-size:23px;color:#fff}
  .contact .item{display:flex;align-items:center;gap:8px}
  .contact .sep{width:2px;height:26px;background:rgba(255,255,255,.7)}
</style>
</head>
<body>
<div class="stage">
  <div class="flyer">
    <svg class="shapes" width="1058" height="1495" viewBox="0 0 1058 1495" aria-hidden="true">
      <defs>
        <linearGradient id="strip" x1="0" x2="1"><stop offset="0" stop-color="#079fd5"/><stop offset="1" stop-color="#17b6d4"/></linearGradient>
      </defs>
      <polygon points="0,173 505,173 560,527 560,550 0,550" fill="var(--cyan)"/>
      <rect x="0" y="527" width="1058" height="23" fill="url(#strip)"/>
      <polygon points="0,773 505,773 595,1365 0,1365" fill="var(--navy)"/>
      <rect x="0" y="1365" width="1058" height="78" fill="var(--cyan)"/>
      <polygon points="0,1443 618,1443 626,1495 0,1495" fill="var(--navy)"/>
    </svg>

    <svg class="photo" width="1058" height="527" viewBox="0 0 1058 527" role="img" aria-label="Aerial photo of a tiled house roof covered with solar panels above green gardens">
      <defs>
        <linearGradient id="roof" x1="0" y1="0" x2="1" y2="1">
          <stop offset="0" stop-color="var(--photo-garden)"/><stop offset="0.45" stop-color="var(--photo-roof)"/><stop offset="1" stop-color="#2e3140"/>
        </linearGradient>
      </defs>
      <polygon points="492,0 1058,0 1058,527 573,527" fill="url(#roof)"/>
    </svg>

    <svg class="photo" width="1058" height="1365" viewBox="0 0 1058 1365" role="img" aria-label="Aerial photo of suburban homes with rooftop solar panels">
      <defs>
        <linearGradient id="homes" x1="0" y1="0" x2="0" y2="1">
          <stop offset="0" stop-color="#8a9a9a"/><stop offset="0.5" stop-color="#4b5366"/><stop offset="1" stop-color="var(--photo-garden)"/>
        </linearGradient>
      </defs>
      <polygon points="540,1012 1058,1012 1058,1365 595,1365" fill="url(#homes)"/>
    </svg>

    <div class="brand"><span class="brand-mark"></span><span class="brand-name">brightvale</span></div>

    <h1 class="headline">SOLAR FOR $0<br>DOWN.<br>NO LIENS.<br>NO KIDDING.</h1>
    <p class="tagline">Power Your Future with<br>Brightvale Energy</p>

    <div class="rule" style="left:101px;width:322px"></div>
    <div class="rule" style="left:637px;width:322px"></div>
    <h2 class="section-title">ABOUT US</h2>
    <p class="about-text">At Brightvale Energy, our mission is to make solar simple and accessible for everyone. No high-pressure sales-just the information you need to make a smart choice. With our solar rental program, you can lower your monthly energy costs and pay less than your current electricity bill.</p>

    <div class="tab" style="left:101px">OUR BEST SERVICE</div>
    <div class="tab" style="left:585px">WHY CHOOSE US?</div>

    <div class="services">
      <div class="service" style="top:0">
        <svg width="80" height="92" viewBox="0 0 80 92" aria-hidden="true">
          <polygon points="40,2 77,24 77,68 40,90 3,68 3,24" fill="var(--navy)" stroke="var(--teal)" stroke-width="5"/>
          <polygon points="40,14 66,30 66,62 40,78 14,62 14,30" fill="#fff"/>
          <circle cx="40" cy="40" r="13" fill="var(--navy)"/>
          <text x="40" y="47" text-anchor="middle" font-family="Montserrat,sans-serif" font-weight="700" font-size="19" fill="#fff">$</text>
          <path d="M32 56 L40 66 L48 56" fill="none" stroke="var(--navy)" stroke-width="4"/>
        </svg>
        <div><h3>Expert Installation</h3><p>Certified professionals handle installation, maintenance, and repairs end to end.</p></div>
      </div>
      <div class="service" style="top:127px">
        <svg width="80" height="92" viewBox="0 0 80 92" aria-hidden="true">
          <polygon points="40,2 77,24 77,68 40,90 3,68 3,24" fill="var(--navy)" stroke="var(--teal)" stroke-width="5"/>
          <polygon points="40,14 66,30 66,62 40,78 14,62 14,30" fill="#fff"/>
          <circle cx="40" cy="44" r="13" fill="none" stroke="var(--navy)" stroke-width="4"/>
          <circle cx="40" cy="44" r="5" fill="var(--navy)"/>
          <path d="M32 55 L28 68 L36 64 M48 55 L52 68 L44 64" fill="none" stroke="var(--navy)" stroke-width="3"/>
        </svg>
        <div><h3>Eco-Friendly</h3><p>Clean, renewable solar energy that helps reduce your carbon footprint.</p></div>
      </div>
      <div class="service" style="top:251px">
        <svg width="80" height="92" viewBox="0 0 80 92" aria-hidden="true">
          <polygon points="40,2 77,24 77,68 40,90 3,68 3,24" fill="var(--navy)" stroke="var(--teal)" stroke-width="5"/>
          <polygon points="40,14 66,30 66,62 40,78 14,62 14,30" fill="#fff"/>
          <circle cx="40" cy="46" r="15" fill="none" stroke="var(--navy)" stroke-width="7" stroke-dasharray="5 4.4"/>
          <circle cx="40" cy="46" r="10" fill="var(--navy)"/>
          <circle cx="40" cy="46" r="4" fill="#fff"/>
        </svg>
        <div><h3>Affordable &amp; Transparent</h3><p>Simple pricing, no hidden fees and a fixed monthly rate lower than typical energy bills.</p></div>
      </div>
      <div class="service" style="top:370px">
        <svg width="80" height="92" viewBox="0 0 80 92" aria-hidden="true">
          <polygon points="40,2 77,24 77,68 40,90 3,68 3,24" fill="var(--navy)" stroke="var(--teal)" stroke-width="5"/>
          <polygon points="40,14 66,30 66,62 40,78 14,62 14,30" fill="#fff"/>
          <path d="M40 52 C28 50 24 40 26 32 C36 34 40 42 40 52 C40 42 44 34 54 32 C56 40 52 50 40 52 Z" fill="var(--navy)"/>
          <path d="M22 56 C32 56 38 62 50 60 L58 56" fill="none" stroke="var(--navy)" stroke-width="4"/>
        </svg>
        <div><h3>Local Expertise</h3><p>Florida-based team that understands the<br>needs of Orlando and statewide homeowners.</p></div>
      </div>
    </div>

    <ul class="benefits">
      <li><svg width="16" height="16" viewBox="0 0 16 16" aria-hidden="true"><circle cx="8" cy="8" r="8" fill="var(--cyan)"/><path d="M4.5 8.2 L7 10.5 L11.5 5.5" fill="none" stroke="#fff" stroke-width="2"/></svg>No financing</li>
      <li><svg width="16" height="16" viewBox="0 0 16 16" aria-hidden="true"><circle cx="8" cy="8" r="8" fill="var(--cyan)"/><path d="M4.5 8.2 L7 10.5 L11.5 5.5" fill="none" stroke="#fff" stroke-width="2"/></svg>No liensNo down payment</li>
      <li><svg width="16" height="16" viewBox="0 0 16 16" aria-hidden="true"><circle cx="8" cy="8" r="8" fill="var(--cyan)"/><path d="M4.5 8.2 L7 10.5 L11.5 5.5" fill="none" stroke="#fff" stroke-width="2"/></svg>No insurance costs</li>
      <li><svg width="16" height="16" viewBox="0 0 16 16" aria-hidden="true"><circle cx="8" cy="8" r="8" fill="var(--cyan)"/><path d="M4.5 8.2 L7 10.5 L11.5 5.5" fill="none" stroke="#fff" stroke-width="2"/></svg>No long-term commitment</li>
      <li><svg width="16" height="16" viewBox="0 0 16 16" aria-hidden="true"><circle cx="8" cy="8" r="8" fill="var(--cyan)"/><path d="M4.5 8.2 L7 10.5 L11.5 5.5" fill="none" stroke="#fff" stroke-width="2"/></svg>No maintenance costs</li>
    </ul>

    <div class="contact">
      <span class="item"><svg width="22" height="22" viewBox="0 0 22 22" aria-hidden="true"><circle cx="11" cy="11" r="11" fill="#fff"/><path d="M7 6 L9 6 L10 9 L8.8 10 C9.5 11.6 10.5 12.6 12 13.2 L13 12 L16 13 L16 15 C16 15.8 15.2 16.3 14.4 16.1 C10.4 15.2 6.9 11.7 6 7.6 C5.8 6.8 6.3 6 7 6 Z" fill="var(--cyan)"/></svg>(555)010-2040</span>
      <span class="sep"></span>
      <span class="item"><svg width="18" height="24" viewBox="0 0 18 24" aria-hidden="true"><path d="M9 1 C4.6 1 1.5 4.2 1.5 8.4 C1.5 14 9 23 9 23 C9 23 16.5 14 16.5 8.4 C16.5 4.2 13.4 1 9 1 Z" fill="#fff"/><circle cx="9" cy="8.5" r="3.2" fill="var(--cyan)"/></svg>123 Anywhere St., Any City</span>
      <span class="sep"></span>
      <span class="item"><svg width="22" height="22" viewBox="0 0 22 22" aria-hidden="true"><circle cx="11" cy="11" r="11" fill="#fff"/><circle cx="11" cy="11" r="6.5" fill="none" stroke="var(--cyan)" stroke-width="1.4"/><ellipse cx="11" cy="11" rx="2.8" ry="6.5" fill="none" stroke="var(--cyan)" stroke-width="1.4"/><path d="M4.5 11 H17.5" stroke="var(--cyan)" stroke-width="1.4"/></svg>www.brightvaleenergy.com</span>
    </div>
  </div>
</div>
</body>
</html>
```